CD Cover Design Project

Project 2 CD cover design. One in English and one in Chinese. (I can provide the Chinese in PDF or any file if necessary.)
I will use the same design for 6 different CD cover with different title only. They all are related to my business-hypnosis.
I have Logo and the main content of the picture for you to design a cover.
I hope the whole design look like all while in a distance but only the title words show up. When you look closely you can see the design-the bird.
Will decide ASAP.
Target Market(s)
My students and audiences in hypnotist training courses.
Customer from my website and my hypnosis office.
Attendee in my lecture and conference.
Industry/Entity Type
Business
Requirements
Must have
- 1. It should looks close to white when been seen in a distance or first sight.
You can make my art work almost disappear or change to an idea like this Letter printing design.
Please visit:
http://plinkzap.example/images/pear_letterpress_macro.jpg
http://www.corvamid.example/wp-content/uploads/2007/02/letterpress_2.jpg
2.About my logo.
Please use only the Bird sign but not the rest of the name and address.
Please have this information about the publisher on the other side:
"Self-hypnosis for Relaxation"
p.s. You can change the size and font and colour any way you wish.
This will be the other side of the cover.
Thank you.
CD Cover ,back, contain information-
Self-hypnosis for Relaxation
Benefits about Self hypnosis. You can fall back to sleep so much easier every night! Keeps a sense of logic and ease of mind every day. It gives you the control of your emotions and situations. You can apply it on daily business.
To help yourself to go into the deeper hypnotic trance easily you need to five yourself permission to dream, fantasize and play before allowing your rational mind to do the necessary job of sorting, assessing and figuring out hot to act upon the information that you receive. Many of us rationalize or criticize too quickly, without giving our intuition the time and space it deserve.
To give your self permission to use your imagination constructively and to open your mind and emotions to a newer ability, here are some suggestions for you to use. They are simple but powerful positive affirmations that gently help to alter your beliefs, habits and expectation toward your foal. When used on a regular basis is that they will help to make you more available for some experiences and less available for others. The power of this self-hypnosis is strong: what we ask for, we often receive.
Lie down with your back fully supported or sit comfortable in a quiet place.
Relax and breathe easily and deeply. Every time you breathe out, you feel more relaxed.
Count from 10 to 1, at each count you feel even more relax. At the last count, hold your breath and count for 3 seconds then let go, breathe out.
Read in your mind 10 times the following statement. In order not to full asleep, move your fingers while counting from the right hand to the left.
I’m calm. I’m relax. I’m in control.
ADD LOGO HERE
Fern Trance
www.ferntrance.example Ontario, Canada (555) 246-3187
- end -
Nice to have
- Clean and quiet, spiritual.
This is my both English and Chinese website. Please check it out even you might not read Chinese. All of the picture and art works are done by myself.
www.ferntrance.example
www.tw.ferntrance.example

```html
<!DOCTYPE html>
<html lang="en">
<head>
<meta charset="utf-8">
<title>Good Night Sleep – CD Cover</title>
<link href="https://fonts.googleapis.com/css2?family=Roboto+Condensed:wght@300;400&family=Kalam:wght@300&display=swap" rel="stylesheet">
<style>
  :root{
    --backdrop:#e8e5e1;
    --sheet:#ffffff;
    --panel:#fbfbfb;
    --bleed:#f08fc8;
    --trim:#2fb6e8;
    --ink:#6d645a;
    --ink-soft:#8a8279;
    --title:#6b5f52;
    --card-top:#ffffff;
    --card-bottom:#c7c0b5;
    --art:#eceae8;
  }
  *{margin:0;padding:0;box-sizing:border-box}
  html,body{width:1200px;height:1000px;overflow:hidden;background:var(--backdrop)}
  .canvas{position:relative;width:1200px;height:1000px}
  .sheet{position:absolute;left:32px;top:170px;width:1132px;height:563px;background:var(--sheet)}
  .guides{position:absolute;left:0;top:0}
  .artwork{position:absolute;border-radius:50%;background:radial-gradient(closest-side,var(--art),rgba(236,234,232,0))}
  .artwork--back{left:160px;top:260px;width:420px;height:420px}
  .artwork--front{left:660px;top:240px;width:440px;height:420px}
  .back-copy{position:absolute;left:138px;top:243px;width:372px;font-family:"Roboto Condensed",sans-serif;font-weight:300;font-size:9.2px;line-height:12.3px;color:var(--ink)}
  .back-copy h1{font-weight:300;font-size:9.6px;margin-bottom:11px}
  .back-copy .affirmation{font-style:italic;margin-top:12px}
  .publisher{position:absolute;left:80px;top:614px;font-family:"Roboto Condensed",sans-serif;font-weight:300;font-size:9.4px;line-height:12.4px;color:var(--ink-soft)}
  .spine-title{position:absolute;left:597px;top:448px;transform:translate(-50%,-50%) rotate(90deg);font-family:"Kalam",cursive;font-weight:300;font-size:12px;color:var(--ink);white-space:nowrap}
  .front-card{position:absolute;left:720px;top:240px;width:312px;height:415px;background:var(--panel);box-shadow:0 0 6px rgba(0,0,0,.08)}
  .brand{position:absolute;left:735px;top:560px;display:flex;align-items:center;gap:5px;font-family:"Roboto Condensed",sans-serif;font-weight:400;font-size:10px;color:#222}
  .brand-dot{width:9px;height:9px;border-radius:50%;background:#222}
  .ribbon{position:absolute;left:690px;top:586px}
  .ribbon-title{position:absolute;left:692px;top:588px;width:365px;height:46px;line-height:46px;text-align:center;font-family:"Kalam",cursive;font-weight:300;font-size:27px;color:var(--title)}
</style>
</head>
<body>
<div class="canvas">
  <div class="sheet"></div>

  <div class="artwork artwork--back" role="img" aria-label="Faint embossed bird artwork, white on white"></div>
  <div class="artwork artwork--front" role="img" aria-label="Faint embossed bird artwork across the front cover"></div>

  <svg class="guides" width="1200" height="1000" aria-hidden="true">
    <defs>
      <linearGradient id="cardFade" x1="0" y1="0" x2="0" y2="1">
        <stop offset="0" stop-color="var(--card-top)"/>
        <stop offset=".55" stop-color="#f4f2ef"/>
        <stop offset="1" stop-color="var(--card-bottom)"/>
      </linearGradient>
      <linearGradient id="ribbonFace" x1="0" y1="0" x2="0" y2="1">
        <stop offset="0" stop-color="#ffffff"/>
        <stop offset=".6" stop-color="#ececec"/>
        <stop offset="1" stop-color="#cfcfcf"/>
      </linearGradient>
    </defs>
    <rect x="62" y="204" width="1075" height="489" fill="none" stroke="var(--bleed)" stroke-width="1" stroke-dasharray="3 2"/>
    <rect x="70" y="214" width="1055" height="469" fill="none" stroke="var(--trim)" stroke-width="1.2"/>
    <line x1="586" y1="214" x2="586" y2="683" stroke="var(--trim)" stroke-width="1.2"/>
    <line x1="608" y1="214" x2="608" y2="683" stroke="var(--trim)" stroke-width="1.2"/>
    <line x1="591" y1="204" x2="591" y2="693" stroke="var(--bleed)" stroke-dasharray="3 2"/>
    <line x1="603" y1="204" x2="603" y2="693" stroke="var(--bleed)" stroke-dasharray="3 2"/>
    <path d="M115 222 H528 V548 Q528 564 512 566 L132 590 Q115 592 115 575 Z" fill="url(#cardFade)"/>
    <g transform="translate(0,0)">
      <path d="M692 590 H1057 V634 H692 Z" fill="url(#ribbonFace)"/>
      <path d="M692 634 L720 646 V634 Z" fill="#a9a9a9"/>
      <path d="M1057 634 L1032 646 V634 Z" fill="#a9a9a9"/>
      <line x1="692" y1="590" x2="1057" y2="590" stroke="#e2e2e2"/>
    </g>
  </svg>

  <article class="back-copy">
    <h1>Self-hypnosis for Relaxation</h1>
    <p>Benefits about Self hypnosis. You can fall back to sleep so much easier every night!&nbsp; Keeps a sense of logic and ease of mind every day.&nbsp; It gives you the control of your emotions and situations.&nbsp; You can apply it on daily business.</p>
    <p>To help yourself to go into the deeper hypnotic trance easily you need to five yourself permission to dream, fantasize and play before allowing your rational mind to do the necessary job of sorting, assessing and figuring out hot to act upon the information that you receive. Many of us rationalize or criticize too quickly, without giving our intuition the time and space it deserve.</p>
    <p>To give your self permission to use your imagination constructively and to open your mind and emotions to a newer ability, here are some suggestions for you to use. They are simple but powerful positive affirmations that gently help to alter your beliefs, habits and expectation toward your foal. When used on a regular basis is that they will help to make you more available for some experiences and less available for others. The power of this self-hypnosis is strong: what we ask for, we often receive.</p>
    <p>Lie down with your back fully supported or sit comfortable in a quiet place.</p>
    <p>Relax and breathe easily and deeply. Every time you breathe out, you feel more relaxed.</p>
    <p>Count from 10 to 1, at each count you feel even more relax. At the last count, hold your breath and count for 3 seconds then let go, breathe out.</p>
    <p>Read in your mind 10 times the following statement. In order not to full asleep, move your fingers while counting from the right hand to the left.</p>
    <p class="affirmation">I’m calm.&nbsp; I’m relaxed.&nbsp; I’m in control.</p>
  </article>

  <address class="publisher" style="font-style:normal">
    Hypnosis Series No. EA-20131001<br>
    2013 Published by Fern Trance<br>
    1200 Maple Rd., Suite 40, Lakeview, Ontario A1B 2C3, Canada<br>
    www.ferntrance.example hello@ferntrance.example (555) 246-3187
  </address>

  <div class="spine-title">Good Night Sleep</div>

  <div class="front-card"></div>
  <div class="brand"><span class="brand-dot"></span>Fern Trance</div>
  <div class="ribbon-title">Good Night Sleep</div>
</div>
</body>
</html>
```